Business Card Design - TORVEX
miles@torvex.example
Project: Business Card Design - TORVEX
Business Card Design - TORVEX - Telecommunications
Creative Brief
Professional
Miles Brandt
Vice President
www.torvex.example
Looking for a very well designed and eye catching business card that we can use into the future. Should be designed around the TORVEX logo and using the included radio images is just optional.
Digital Communications Coastline Fleet Relay Grid Cellphone Coverage Enhancement P25 - Public Safety Equipment Digital Radio Rentals Dispatch Consoles
milestor7 milestor7
Thanks for all the design ideas so far. I will be getting together with my team and will start providing feedback this afternoon. Best Wishes, Miles

```html
<!DOCTYPE html>
<html lang="en">
<head>
<meta charset="utf-8">
<title>TORVEX Stationery</title>
<link href="https://fonts.googleapis.com/css2?family=Montserrat:wght@400;500;600;700&display=swap" rel="stylesheet">
<style>
:root{
  --bg:#e9e9e9;
  --paper:#ffffff;
  --ink:#1d1d1d;
  --text:#3a3a3a;
  --muted:#8a8a8a;
  --red:#c8202a;
  --black:#151515;
}
*{margin:0;padding:0;box-sizing:border-box}
html,body{width:1200px;height:859px;overflow:hidden;background:var(--bg);font-family:"Montserrat",sans-serif;color:var(--text)}
.canvas{position:relative;width:1200px;height:859px}
.sheet{position:absolute;background:var(--paper);box-shadow:0 2px 8px rgba(0,0,0,.18);overflow:hidden}
.brand{display:flex;align-items:center;gap:6px;font-weight:700;color:var(--ink);letter-spacing:3px}
.brand .mark{width:9px;height:9px;background:var(--red)}
.brand.light{color:#fff}
.bars{position:absolute;left:0;right:0;bottom:0;display:flex}
.bars .r{background:var(--red);flex:0 0 38%}
.bars .k{background:var(--black);flex:1}

/* letterhead */
.letterhead{left:96px;top:50px;width:317px;height:771px;padding:0 22px}
.letterhead .brand{position:absolute;top:42px;left:0;right:0;justify-content:center;font-size:22px}
.recipient{position:absolute;top:140px;left:22px;font-size:6.5px;line-height:10px;color:var(--ink)}
.recipient .to{margin-bottom:12px}
.letter-body{position:absolute;top:225px;left:22px;right:22px;font-size:5.6px;line-height:9px;text-align:justify}
.letter-body h2{font-size:7.5px;font-weight:700;color:var(--ink);margin-bottom:4px}
.letter-body p{margin-bottom:10px}
.closing{position:absolute;top:668px;left:22px;font-size:6px;color:var(--ink)}
.signature{display:block;margin-top:12px;width:40px;height:12px;background:linear-gradient(90deg,#bbb,#ddd);border-radius:6px}
.letter-foot{position:absolute;left:22px;right:22px;bottom:14px;display:flex;justify-content:space-between;font-size:6px;color:var(--ink)}
.letter-foot b{color:var(--red);font-weight:600}
.letterhead .bars{height:6px}

/* business cards */
.card{top:106px;width:129px;height:144px}
.card-front{left:700px}
.card-front .brand{position:absolute;top:40px;left:0;right:0;justify-content:center;font-size:13px;letter-spacing:2px}
.card-front .brand .mark{width:6px;height:6px}
.person{position:absolute;left:10px;top:96px;font-size:5px;line-height:7px;color:var(--ink)}
.person strong{display:block;font-size:6px;font-weight:700}
.person span{color:var(--red)}
.card-contact{position:absolute;left:66px;top:92px;font-size:4.4px;line-height:8px;color:var(--ink)}
.card-contact b{color:var(--red)}
.card .bars{height:5px}
.card-back{left:851px;width:139px;background:var(--black)}
.card-back .brand{position:absolute;top:64px;left:9px;font-size:10px;letter-spacing:1.5px}
.card-back .brand .mark{width:5px;height:5px}
.divider{position:absolute;left:66px;top:34px;width:1px;height:78px;background:var(--red)}
.services{position:absolute;left:71px;top:38px;list-style:none;font-size:3.4px;line-height:7px;color:#ddd;text-transform:uppercase;font-weight:600}
.services li::before{content:"";display:inline-block;width:3px;height:1px;background:var(--red);margin-right:3px;vertical-align:middle}

/* envelopes */
.envelope{left:703px;width:288px}
.env-back{top:336px;height:187px}
.env-back svg{position:absolute;left:0;top:0}
.env-front{top:569px;height:194px}
.env-front .brand{position:absolute;top:28px;left:12px;font-size:19px}
.env-contact{position:absolute;left:12px;top:150px;font-size:5.6px;line-height:8.5px;color:var(--ink)}
.env-contact b{color:var(--red)}
.window{position:absolute;right:18px;bottom:24px;width:82px;height:42px;border:1px solid #bdbdbd}
.env-front .bars{height:6px}
</style>
</head>
<body>
<div class="canvas">

  <section class="sheet letterhead">
    <div class="brand"><span class="mark"></span>TORVEX</div>
    <div class="recipient">
      <div class="to">To,</div>
      <div>Harlow</div>
      <div>Director</div>
      <div>The Customer</div>
      <div><b>A.</b> 123 456 789</div>
      <div><b>B.</b> 123 456 789</div>
    </div>
    <div class="letter-body">
      <h2>Lorem ipsum dolor sit amet</h2>
      <p>Lorem ipsum dolor sit amet, consectetur adipiscing elit. Quisque pellentesque, nunc nec semper ullamcorper, enim eros sodales quam, eu ullamcorper felis neque vel lacus. Proin nec pharetra velit, in blandit enim. Mauris molestie, tortor eu rutrum semper, magna odio ultricies libero, quis egestas turpis magna sed nisl. Integer sagittis purus nec ante semper, vitae volutpat est vestibulum. Donec sed suscipit sapien. Maecenas vestibulum dui diam, mattis suscipit purus hendrerit id. In nisl mi, consequat eget nibh sed, tristique malesuada leo. Vestibulum convallis quam non nisl sollicitudin cursus non at felis. In efficitur eros sed porta interdum. Phasellus tempus risus nibh, quis ornare elit rhoncus et. Aliquam erat volutpat. Fusce id enim lectus.</p>
      <p>Integer ac facilisis nibh, eu suscipit nibh. Curabitur efficitur velit nec luctus dictum. Quisque sit amet sodales ligula. Vestibulum vel mi ac nunc ullamcorper finibus, urna felis sagittis risus, at vestibulum sem felis nec mi. In odio lorem, vulputate vitae dignissim quis, gravida id turpis. Cras pulvinar quis augue eu dignissim. Phasellus semper enim at augue malesuada sollicitudin. Duis et sagittis erat, vitae fermentum leo. Nunc a ligula dapibus, cursus orci vitae, facilisis nisl.</p>
    </div>
    <div class="closing">Regards,<span class="signature" role="img" aria-label="Handwritten signature"></span></div>
    <div class="letter-foot">
      <span><b>T :</b> 555-014-2290</span>
      <span><b>E :</b> miles@torvex.example</span>
      <span><b>W :</b> www.torvex.example</span>
    </div>
    <div class="bars" style="bottom:0"><span class="r"></span><span class="k"></span></div>
  </section>

  <section class="sheet card card-front">
    <div class="brand"><span class="mark"></span>TORVEX</div>
    <div class="person"><strong>Miles Brandt</strong><span>Vice President</span></div>
    <div class="card-contact">
      <div><b>T :</b> 555-014-2290</div>
      <div><b>E :</b> miles@torvex.example</div>
      <div><b>W :</b> www.torvex.example</div>
    </div>
    <div class="bars"><span class="r"></span><span class="k"></span></div>
  </section>

  <section class="sheet card card-back">
    <div class="brand light"><span class="mark"></span>TORVEX</div>
    <span class="divider"></span>
    <ul class="services">
      <li>Digital Communications</li>
      <li>Coastline Fleet Relay Grid</li>
      <li>Cellphone Coverage Enhancement</li>
      <li>P25 - Public Safety Equipment</li>
      <li>Digital Radio Rentals</li>
      <li>Dispatch Consoles</li>
    </ul>
  </section>

  <section class="sheet envelope env-back">
    <svg width="288" height="187" viewBox="0 0 288 187">
      <polygon points="0,0 288,0 144,78" fill="#151515"/>
      <polyline points="0,0 144,78 288,0" fill="none" stroke="#c8202a" stroke-width="2"/>
      <line x1="0" y1="187" x2="144" y2="96" stroke="#dddddd" stroke-width="1"/>
      <line x1="288" y1="187" x2="144" y2="96" stroke="#dddddd" stroke-width="1"/>
    </svg>
  </section>

  <section class="sheet envelope env-front">
    <div class="brand"><span class="mark"></span>TORVEX</div>
    <div class="env-contact">
      <div><b>T :</b> 555-014-2290</div>
      <div><b>E :</b> miles@torvex.example</div>
      <div><b>W :</b> www.torvex.example</div>
    </div>
    <div class="window"></div>
    <div class="bars"><span class="r"></span><span class="k"></span></div>
  </section>

</div>
</body>
</html>
```